Create a landing page for a new product market combination for an international software company

We are a software company being in the BtoB market for over 20 years. Our product is a software tool that allows for very flexible and versatile cost calculations for companies. We sell to all industries in over 40 countries with 500 clients. We have fairly recently seen a succesfull "competitor" (www.quorvel.com) come up in the niche market of IT costing. This competitor has launched an independent platform with regards to managing IT costs (www.PLXguild.org). In this independent platform standards are set, events are organised and books are written. Since our software can handle all type of costing questions we can en already do play a role in IT costing. We have therefore become a sponsor of the PLX guild. Besides that we came accross the opportunity to buy the URL: www.plxsoftware.com Which we did. We are now looking for a design on that landing page that communicates the fact that the visitor has landed with a company that have in depth knowledge on the PLX subject and provide an effective an affordable tooling for PLX. Currently the difference between the professionalism of our own website (www.brandivex.com) and that of the competitor (www.quorvel.com) and the independent council (www.plxguild.org). is too big.

Target Market(s)

BtB with large IT spend

Number of Pages Required

1 page

Colors

Designer to choose colors to be used in the design.

Requirements
Must have
• A proffessional look and feel
Should not have
• Definetely not too much information and wording

```html
<!DOCTYPE html>
<html lang="en">
<head>
<meta charset="utf-8">
<title>Brandivex – PLX tooling</title>
<link href="https://fonts.googleapis.com/css2?family=Roboto:wght@400;500;700&display=swap" rel="stylesheet">
<style>
:root{
  --navy:#0c1e5b;
  --night:#0b1a3d;
  --orange:#e2661f;
  --peach:#edb48f;
  --slate:#7e8aa8;
  --ink:#222;
  --grey:#444;
  --rule:#c9c9c9;
  --footer:#0b0b0b;
  --white:#fff;
}
*{box-sizing:border-box;margin:0;padding:0}
html,body{width:1200px;height:2886px;overflow:hidden}
body{position:relative;background:var(--white);font-family:'Roboto',sans-serif;color:var(--ink)}
.abs{position:absolute}
.hero{position:absolute;left:10px;top:0;width:1180px;height:494px}
.hero-bg{position:absolute;inset:0}
.brand{left:10px;top:10px;color:var(--white);font-size:23px;font-weight:500}
.nav{left:314px;top:14px;display:flex;font-size:14px;color:var(--white)}
.nav a{color:var(--white);text-decoration:none;margin-right:27px;padding:2px 0}
.nav a.active{border-bottom:2px solid var(--white)}
.nav a.contact{background:var(--orange);padding:3px 8px;border-radius:3px;margin-right:0}
.search{left:949px;top:9px;width:242px;height:36px;background:var(--white);border:1px solid #bbb;font-size:14px;color:#888;padding:9px 10px}
.search span{position:absolute;right:0;top:0;width:28px;height:34px;background:#ccc}
.hero-title{left:10px;top:208px;width:1180px;text-align:center;color:var(--white);font-size:29px;font-weight:700;line-height:38px}
.btn-ask{left:497px;top:290px;width:203px;height:43px;background:var(--orange);color:var(--white);font-size:27px;font-weight:500;text-align:center;line-height:43px}
.section-title{width:1200px;text-align:center;font-size:23px;font-weight:500;color:var(--ink)}
.section-title em{font-style:normal;color:var(--orange)}
.title-shadow{left:540px;width:120px;height:8px;border-radius:50%;background:radial-gradient(ellipse,rgba(0,0,0,.22),rgba(0,0,0,0) 70%)}
.lead{left:200px;top:606px;width:800px;text-align:center;font-size:13.5px;line-height:29px;color:var(--grey)}
.card-photo{height:159px;top:674px;width:228px}
.card-text{top:843px;width:235px;font-size:11.5px;line-height:14px;color:var(--grey)}
.card-text b{color:var(--ink);font-weight:500;display:block}
.card-text b::first-letter{font-size:14px}
.why{top:1025px;font-size:24px}
.circle{width:242px;height:287px;border-radius:50%}
.band{left:205px;top:1158px;width:790px;height:178px;background:var(--white)}
.reason-label{top:1129px;width:242px;text-align:center;font-size:12.5px;font-weight:500;color:var(--ink)}
.reason-label::after{content:"";display:block;width:70px;height:2px;background:var(--ink);margin:5px auto 0}
.reason-text{top:1188px;width:245px;font-size:11.5px;line-height:14px;color:var(--grey);height:100px;overflow:hidden}
.divider{top:1190px;width:1px;height:98px;background:var(--rule)}
.hr{left:412px;top:1443px;width:405px;height:1px;background:var(--rule)}
.support-title{left:296px;top:1574px;color:var(--white);font-size:23px;font-weight:500}
.support-note{left:234px;top:1617px;color:var(--white);font-size:12px}
.field{left:234px;width:405px;height:40px;background:#f7f7f7;border:1px solid #ddd;border-radius:3px;font-size:13px;color:#999;padding:11px 14px}
.submit{left:234px;top:1757px;width:203px;height:38px;background:var(--orange);color:var(--white);font-size:13px;font-weight:500;text-align:center;line-height:38px;border-radius:2px}
.group{left:213px;font-size:22px;font-weight:500;color:var(--ink)}
.partner{width:170px;height:60px;display:flex;align-items:center;justify-content:center;gap:8px;font-size:19px;font-weight:500;color:var(--navy);white-space:nowrap}
.partner i{display:block;width:12px;height:12px;background:var(--orange)}
.more{left:852px;width:128px;height:30px;background:var(--orange);border:2px solid #5a2a0c;color:var(--navy);font-size:20px;font-weight:500;text-align:center;line-height:26px}
.footer{left:10px;top:2693px;width:1180px;height:187px;background:var(--footer)}
.foot-head{color:var(--white);font-size:13px;font-weight:700;display:flex;align-items:center;gap:8px}
.foot-head i{display:block;width:11px;height:11px;border-radius:50%;background:var(--orange)}
.copyright{left:0;top:2835px;width:1200px;text-align:center;color:var(--white);font-size:16px}
</style>
</head>
<body>

<header class="hero">
  <svg class="hero-bg" width="1180" height="494" viewBox="0 0 1180 494" role="img" aria-label="Night skyline of a city with lit office towers">
    <defs>
      <linearGradient id="sky" x1="0" y1="0" x2="0" y2="1">
        <stop offset="0" stop-color="#0e2a6e"/>
        <stop offset=".55" stop-color="#15306a"/>
        <stop offset="1" stop-color="#0a1630"/>
      </linearGradient>
    </defs>
    <rect width="1180" height="494" fill="url(#sky)"/>
    <polygon points="0,494 1180,378 1180,494" fill="#fff"/>
    <line x1="0" y1="494" x2="1180" y2="378" stroke="#333" stroke-width="2"/>
  </svg>
</header>

<div class="abs brand">Brandivex</div>
<nav class="abs nav">
  <a class="active">Home</a><a>Product</a><a>Markets</a><a>Company</a><a>Partners</a><a>Events</a><a>Support</a><a class="contact">Contact</a>
</nav>
<div class="abs search">Search<span></span></div>

<h1 class="abs hero-title">In depth knowledge on PLX in Brandivex and provide an effective<br>and affordable tooling for PLX.</h1>
<div class="abs btn-ask">Ask Question</div>

<h2 class="abs section-title" style="top:554px"><em>Our</em> Product</h2>
<div class="abs title-shadow" style="top:586px"></div>
<p class="abs lead">Our product is a software tool that allows for very flexible and versatile cost calculations for companies. We sell to all industries in over 40 countries with 500 clients.</p>

<div class="abs card-photo" style="left:213px;background:linear-gradient(135deg,#c9d3e0,#7c8aa3)" role="img" aria-label="Business team around a digital network graphic"></div>
<div class="abs card-photo" style="left:490px;background:linear-gradient(135deg,#e8e2d8,#9a8f80)" role="img" aria-label="Two colleagues reviewing documents at a desk"></div>
<div class="abs card-photo" style="left:763px;background:linear-gradient(135deg,#dfe6ee,#8a9bb0)" role="img" aria-label="Office team working together on a laptop"></div>

<div class="abs card-text" style="left:213px"><b>Brandivex to manage your costs, capacity, revenues and margins</b>Since 1992, Valtrisk has played a significant role in helping companies better understand their cost flow. Modeling and communicating causal relationships between a company's output and required cost input has always been the basic added value of the tool.</div>
<div class="abs card-text" style="left:490px"><b>Brandivex to manage your costs, capacity, revenues and margins</b>Since 1992, Valtrisk has played a significant role in helping companies better understand their cost flow. Modeling and communicating causal relationships between a company's output and required cost input has always been the basic added value of the tool.</div>
<div class="abs card-text" style="left:763px"><b>Brandivex to manage your costs, capacity, revenues and margins</b>Since 1992, Valtrisk has played a significant role in helping companies better understand their cost flow. Modeling and communicating causal relationships between a company's output and required cost input has always been the basic added value of the tool.</div>

<h2 class="abs section-title why">Why should <em>you choose</em> our products?</h2>
<div class="abs title-shadow" style="top:1058px;left:520px;width:220px"></div>

<div class="abs circle" style="left:208px;top:1104px;background:var(--peach)"></div>
<div class="abs circle" style="left:479px;top:1104px;background:var(--slate)"></div>
<div class="abs circle" style="left:750px;top:1104px;background:var(--peach)"></div>
<div class="abs band"></div>

<div class="abs reason-label" style="left:208px">Get a grip on costs</div>
<div class="abs reason-label" style="left:479px">Improve Performance</div>
<div class="abs reason-label" style="left:750px">Outsmart Your Competition</div>

<p class="abs reason-text" style="left:213px">Every company wants to improve performance. Success starts with a greater knowledge of how your company works today in terms of costs and capacity. Make your company's cost and capacity flow transparent by using Brandivex's bold graphic user interface and get a grip.</p>
<div class="abs divider" style="left:466px"></div>
<p class="abs reason-text" style="left:484px">Successful companies apply continuous process improvement principles in order to stay ahead of the competition. These principles are simple: increase your sales volume and lower your unit costs through more efficient and effective processes. Brandivex has the tools and expertise your company needs.</p>
<div class="abs divider" style="left:736px"></div>
<p class="abs reason-text" style="left:755px">Today's winners are those companies that stay innovative and keep their unit costs as low as possible. If your company invents a new product or service, it can't wait for competition to kick in and try to copy success. Patent protection does not last forever. Managing the unit costs as an ongoing task.</p>

<div class="abs hr"></div>

<svg class="abs" style="left:213px;top:1491px" width="778" height="398" viewBox="0 0 778 398" aria-hidden="true">
  <polygon points="0,68 778,0 778,330 0,398" fill="var(--navy)"/>
</svg>
<h2 class="abs support-title">Customer Support</h2>
<p class="abs support-note">You can login using the credentials from the installation letter you received.</p>
<div class="abs field" style="top:1652px">Username</div>
<div class="abs field" style="top:1703px">Password</div>
<div class="abs submit">Submit</div>

<h2 class="abs section-title" style="top:1938px"><em>Our</em> Partners</h2>
<div class="abs title-shadow" style="top:1970px"></div>

<h3 class="abs group" style="top:2006px">Dedicated partners</h3>
<div class="abs partner" style="left:200px;top:2076px"><i></i>Brandivex</div>
<div class="abs partner" style="left:410px;top:2090px">Brandivex UK</div>
<div class="abs partner" style="left:620px;top:2073px">Tervano</div>
<div class="abs partner" style="left:830px;top:2073px">Lumora</div>
<div class="abs more" style="top:2156px">View More</div>

<h3 class="abs group" style="top:2204px">Independent consulting</h3>
<div class="abs partner" style="left:200px;top:2286px"><i></i>Harlow &amp; Pike</div>
<div class="abs partner" style="left:410px;top:2286px">Brightfield Group</div>
<div class="abs partner" style="left:620px;top:2290px">Marsten Partners</div>
<div class="abs partner" style="left:830px;top:2290px">Fenwick Metrics</div>
<div class="abs more" style="top:2373px">View More</div>

<h3 class="abs group" style="top:2438px">Affiliates</h3>
<div class="abs partner" style="left:200px;top:2512px">Tidewater Labs</div>
<div class="abs partner" style="left:410px;top:2504px">Northpine</div>
<div class="abs partner" style="left:620px;top:2496px"><i></i>Corvanta</div>
<div class="abs partner" style="left:830px;top:2508px">Selvara</div>
<div class="abs more" style="top:2572px">View More</div>

<footer class="abs footer"></footer>
<div class="abs foot-head" style="left:170px;top:2719px">Quick Menu <i></i></div>
<div class="abs foot-head" style="left:560px;top:2719px">Social Media <i></i></div>
<div class="abs foot-head" style="left:960px;top:2707px">Contact Us <i></i></div>
<p class="abs copyright">© 2019 All right reserved</p>

</body>
</html>
```